A Referral Pad for a Specialist Surgeon to give to referring GPs

A referral pad allows general practitioners to easily refer patients to me by quickly filling in a form on a small pad that I provide them.

A two sided referral pad themed appropriately. Theming and designing the pad should be based on the general design/logo/imagery/colours etc. from my website www.marcusbelwether.com.au. I have a logo uploaded that should be used somewhere. I have also upload a headshot of myself which might or might not be used. Other choice of imagery and design features is up to the designer.

In terms of size of the pad I’m not quite sure what is best and will leave it up to the designers.

MORE DETAILED INFORMATION IS PROVIDED IN THE UPLOADED WORD FILE

Target Market(s)

General Practitioners referring to me

Industry/Entity Type

Healthcare

Contact Information for Business Card

A business card themed as per the referral pad design as as per general look and imagery found on www.marcusbelwether.com.au

Requirements
Must have
• Referral pad details found in uploaded Word document
Nice to have
Should not have

```html
<!DOCTYPE html>
<html lang="en">
<head>
<meta charset="utf-8">
<title>Marcus Belwether – Referral Stationery</title>
<link href="https://fonts.googleapis.com/css2?family=Cormorant+Garamond:wght@400;500;600;700&display=swap" rel="stylesheet">
<style>
:root{
  --teal:#14938a;
  --teal-dark:#0f7a72;
  --teal-soft:#d7eeeb;
  --paper:#f7f8f8;
  --ink:#3d4a4a;
  --muted:#8a9595;
  --backdrop:#e4e7e8;
  --line:#9fb3b1;
}
*{box-sizing:border-box;margin:0;padding:0}
html,body{width:1200px;height:675px;overflow:hidden}
body{background:var(--backdrop);font-family:"Cormorant Garamond",Georgia,serif;color:var(--ink);position:relative}
.sheet{position:absolute;background:var(--paper);box-shadow:0 6px 18px rgba(0,0,0,.12);overflow:hidden}

/* Info sheet */
.info-sheet{left:70px;top:70px;width:340px;height:480px}
.info-band{position:absolute;left:0;top:52px;width:250px;height:58px;background:var(--teal);display:flex;flex-direction:column;justify-content:center;padding-left:22px;color:#fff}
.brand{font-weight:600;letter-spacing:.06em;text-transform:uppercase;font-size:19px;line-height:1}
.brand-sub{font-size:7.5px;letter-spacing:.16em;text-transform:uppercase;margin-top:4px}
.headshot{position:absolute;left:252px;top:40px;width:62px;height:72px;background:linear-gradient(160deg,#6e7c86,#2a3440)}
.info-accent{position:absolute;left:316px;top:60px;width:24px;height:50px;background:var(--teal)}
.info-body{position:absolute;left:26px;top:130px;right:22px}
.section-title{color:var(--teal);font-size:13px;font-weight:600;margin:10px 0 5px}
.dot-list{list-style:none;font-size:9px;line-height:1.45;color:var(--muted)}
.dot-list li{position:relative;padding-left:12px}
.dot-list li::before{content:"";position:absolute;left:0;top:4px;width:6px;height:6px;border-radius:50%;background:var(--teal)}
.info-note{color:var(--teal);font-size:10.5px;font-weight:600;line-height:1.3;margin-top:10px}
.info-web{position:absolute;left:0;right:0;bottom:24px;text-align:center;font-size:9px;letter-spacing:.25em;color:var(--muted)}
.info-foot{position:absolute;left:0;right:0;bottom:0;height:12px;background:var(--teal)}

/* Referral form */
.referral{left:445px;top:70px;width:340px;height:480px}
.ref-brand{position:absolute;right:22px;top:24px;text-align:right;color:var(--teal)}
.ref-brand .brand{font-size:18px}
.ref-brand .brand-sub{font-size:6.5px}
.ref-title{position:absolute;left:22px;top:66px;color:var(--teal);font-size:15px;font-weight:600;letter-spacing:.08em;text-transform:uppercase}
.ref-body{position:absolute;left:22px;right:22px;top:92px;font-size:9px;color:var(--muted)}
.field-row{display:flex;gap:8px;margin-bottom:7px;align-items:flex-end}
.field{flex:1;display:flex;gap:4px;align-items:flex-end;white-space:nowrap}
.field span.rule{flex:1;border-bottom:1px solid var(--line);height:8px}
.ref-section{color:var(--teal);font-size:11px;font-weight:600;margin:8px 0 3px}
.plain-list{list-style:none;line-height:1.55}
.choice{display:flex;align-items:center;justify-content:space-between}
.box{width:8px;height:8px;border:1px solid var(--ink);display:inline-block}
.ref-extra{color:var(--teal);font-size:8.5px;margin-top:4px}
.gp-title{color:var(--teal);font-size:11px;font-weight:600;margin-top:8px}
.ref-foot{position:absolute;left:0;right:0;bottom:0;height:44px;background:var(--teal);color:#fff}
.ref-foot h3{text-align:center;font-size:12px;font-weight:600;padding-top:5px}
.contact-row{display:flex;justify-content:space-around;font-size:8px;margin-top:5px}

/* Business cards */
.card{position:absolute;width:300px;height:170px;box-shadow:0 6px 16px rgba(0,0,0,.14);overflow:hidden}
.card-front{left:840px;top:110px;background:var(--paper)}
.card-front .brand{color:var(--teal);position:absolute;left:26px;top:22px;font-size:17px}
.card-front .brand-sub{color:var(--teal);position:absolute;left:26px;top:42px;font-size:6px}
.card-tab{position:absolute;left:0;top:72px;width:12px;height:30px;background:#9aa3a3}
.card-flag{position:absolute;right:0;top:110px;width:12px;height:28px;background:var(--teal)}
.card-name{position:absolute;left:26px;top:74px;color:var(--teal);font-size:16px;font-weight:600}
.card-details{position:absolute;left:26px;top:98px;list-style:none;font-size:8.5px;color:var(--muted);line-height:1.6}
.card-details li{display:flex;align-items:center;gap:5px}
.card-details svg{width:8px;height:8px}
.card-back{left:840px;top:320px;background:var(--teal);display:flex;flex-direction:column;align-items:center;justify-content:center;color:#fff}
.card-back .brand{font-size:20px}
.card-back .brand-sub{font-size:6.5px}
</style>
</head>
<body>

<section class="sheet info-sheet">
  <div class="info-band">
    <div class="brand">Marcus Belwether</div>
    <div class="brand-sub">General, Upper GI &amp; Bariatric Surgeon</div>
  </div>
  <div class="headshot" role="img" aria-label="Portrait photograph of the surgeon"></div>
  <div class="info-accent"></div>
  <div class="info-body">
    <h2 class="section-title">Bariatric Surgery Procedures Offered</h2>
    <ul class="dot-list">
      <li>Sleeve Gastrectomy</li>
      <li>Gastric Bypass</li>
      <li>Gastric Banding</li>
      <li>Endoscopic surgery</li>
      <li>Revision of prior gastric banding procedures</li>
      <li>Skin removal after major weight loss</li>
    </ul>
    <h2 class="section-title">Standard Eligibility Criteria for Bariatric Surgery</h2>
    <ul class="dot-list">
      <li>BMI &gt; 35 with diabetes or other obesity-related co-morbidity</li>
      <li>BMI &gt; 40 in selected cases</li>
    </ul>
    <h2 class="section-title">Operating Locations</h2>
    <ul class="dot-list">
      <li>Eastvale Private Hospital</li>
      <li>Riverside Private Hospital</li>
      <li>Northgate Public Hospital</li>
      <li>Southbay District Hospital</li>
    </ul>
    <p class="info-note">Please note that for sleeve gastrectomy &amp; gastric bypass procedures, Private health insurance of the appropriate level is mandatory to proceed with surgery.</p>
  </div>
  <div class="info-web">www.marcusbelwether.com.au</div>
  <div class="info-foot"></div>
</section>

<section class="sheet referral">
  <div class="ref-brand">
    <div class="brand">Marcus Belwether</div>
    <div class="brand-sub">General, Upper GI &amp; Bariatric Surgeon</div>
  </div>
  <h1 class="ref-title">Patient Referral</h1>
  <div class="ref-body">
    <div class="field-row"><div class="field">Patient name:<span class="rule"></span></div><div class="field">Referral Date:<span class="rule"></span></div></div>
    <div class="field-row"><div class="field">Phone:<span class="rule"></span></div><div class="field">Date of birth:<span class="rule"></span></div></div>
    <div class="field-row"><div class="field">Email:<span class="rule"></span></div><div class="field">Gender:<span class="rule"></span></div></div>
    <div class="field-row"><div class="field">Medical History/Comments:<span class="rule"></span></div></div>
    <h2 class="ref-section">Consulting Locations</h2>
    <ul class="plain-list">
      <li>1. Melbourne: City rooms, Eastvale, Northgate</li>
      <li>2. Regional: Southbay, Riverside, Lakeview</li>
    </ul>
    <h2 class="ref-section">Procedure Choice</h2>
    <ul class="plain-list">
      <li class="choice">1. Bariatric Surgery (see over for details &amp; eligibility) <span class="box"></span></li>
      <li>&nbsp;&nbsp;a. Patient weight: ______ &nbsp; b. Patient BMI: ______</li>
      <li class="choice">&nbsp;&nbsp;c. Diabetes: Yes <span class="box"></span> No <span class="box"></span><span></span></li>
      <li class="choice">2. Abdominoplasty or Arm Reduction after weight loss <span class="box"></span></li>
      <li class="choice">3. Antireflux/Hiatus Hernia Surgery <span class="box"></span></li>
      <li class="choice">4. Gallbladder <span class="box"></span></li>
      <li class="choice">5. Hernia <span class="box"></span></li>
      <li class="choice">6. Endoscopy <span class="box"></span></li>
      <li>7. Other general surgery: ____________________</li>
    </ul>
    <p class="ref-extra">Includes skin lumps &amp; bumps, peri-anal/haemorrhoids, varicose veins, carpal tunnel</p>
    <h2 class="gp-title">General practitioner details/stamp</h2>
  </div>
  <footer class="ref-foot">
    <h3>Clinic Contact Details</h3>
    <div class="contact-row">
      <span>Fax (03) 9400 1235</span>
      <span>All appointments (03) 9400 1234</span>
      <span>Email: info@belwethersurgery.com.au</span>
    </div>
  </footer>
</section>

<article class="card card-front">
  <div class="brand">Marcus Belwether</div>
  <div class="brand-sub">General, Upper GI &amp; Bariatric Surgeon</div>
  <div class="card-tab"></div>
  <div class="card-name">John Doe</div>
  <ul class="card-details">
    <li><svg viewBox="0 0 8 8"><rect width="8" height="8" fill="#14938a"/></svg>(03) 9400 1234</li>
    <li><svg viewBox="0 0 8 8"><rect width="8" height="8" fill="#14938a"/></svg>info@belwethersurgery.com.au</li>
    <li><svg viewBox="0 0 8 8"><rect width="8" height="8" fill="#14938a"/></svg>www.marcusbelwether.com.au</li>
  </ul>
  <div class="card-flag"></div>
</article>

<article class="card card-back">
  <div class="brand">Marcus Belwether</div>
  <div class="brand-sub">General, Upper GI &amp; Bariatric Surgeon</div>
</article>

</body>
</html>
```